Multifamily Investment Strategies

I need a pamphlet or booklet for multifamily commercial real estate investment.

The specific investment vehicle is affordable multifamily apartments. I have uploaded a 5 page pdf detailing my investment strategy.

The target audience for this pamphlet are investors, commercial brokers, and commercial bankers.

I am looking for modern, clean design that is striking and professional but also eye catching.
Updates

I made a few changes to the brief and also corrected two errors.

Target Market(s)

Commercial Real Estate Investors, Brokers, and Bankers

Industry/Entity Type

Real Estate

Font styles to use
Serif

Colors

Designer to choose colors to be used in the design.

Requirements
Must have
• Graphics of or related to apartment buildings.
• My headshot seen on the last page of the pdf
Nice to have
• Imagery related to investment and profits.
Should not have
• The image of an apartment building on the first page of the pdf is just an example. Please don’t use this image.

```html
<!DOCTYPE html>
<html lang="en">
<head>
<meta charset="utf-8">
<title>Multifamily Cashflow Investment Strategy – Booklet Spread</title>
<link href="https://fonts.googleapis.com/css2?family=Libre+Baskerville:ital,wght@0,400;0,700;1,400&family=Crimson+Text:ital,wght@0,400;0,600;1,400;1,600&display=swap" rel="stylesheet">
<style>
  :root{
    --backdrop:#c4c4c4;
    --slate:#47484b;
    --slate-light:#5a5c60;
    --ink:#3f4043;
    --paper:#ffffff;
    --cyan:#0ea8e6;
    --cyan-deep:#0b95cf;
    --body:#e9e9ea;
  }
  *{box-sizing:border-box;margin:0;padding:0}
  html,body{width:1200px;height:1200px;overflow:hidden;background:var(--backdrop)}
  body{position:relative;font-family:"Crimson Text",Georgia,serif;color:var(--body)}
  .page{position:absolute;background:var(--slate);overflow:hidden;box-shadow:0 4px 10px rgba(0,0,0,.35)}
  .page svg.frame{position:absolute;inset:0;width:100%;height:100%}
  .cover{left:110px;top:30px;width:476px;height:672px}
  .steps{left:623px;top:30px;width:475px;height:672px}
  .finance{left:110px;top:738px;width:306px;height:434px}
  .income{left:450px;top:738px;width:306px;height:434px}
  .author{left:792px;top:738px;width:306px;height:434px}

  .title{position:absolute;font-family:"Libre Baskerville",Georgia,serif;color:var(--ink);letter-spacing:.06em;line-height:1.3}
  .cover .title{left:37px;top:44px;font-size:25.5px;line-height:1.37}
  .running-head{font-size:10.5px;left:24px;top:17px;line-height:1.5}
  .small-head{font-size:7px;left:15px;top:13px;line-height:1.5}

  .tagline{position:absolute;left:37px;top:562px;width:420px;font-family:"Libre Baskerville",Georgia,serif;font-style:italic;color:var(--cyan);font-size:19.5px;line-height:1.33}

  .section-title{position:absolute;font-family:"Libre Baskerville",Georgia,serif;font-style:italic;color:var(--cyan);font-size:18px;left:27px;top:326px}
  .step-head{font-family:"Libre Baskerville",Georgia,serif;font-style:italic;color:var(--cyan);font-size:13px;margin-bottom:10px}
  .col{position:absolute;font-size:8.1px;line-height:1.2;color:var(--body);text-align:justify}
  .col p{margin-bottom:7px}
  .col ul{list-style:none}
  .col li{padding-left:8px;position:relative}
  .col ul.dots li::before{content:"•";position:absolute;left:0}
  .col ol{list-style:none}
  .col ol li{padding-left:10px}
  .col ol li b{position:absolute;left:0;font-weight:600;font-style:italic}
  .col i{font-style:italic;font-weight:600}
  .col-a{left:36px;top:398px;width:200px}
  .col-b{left:250px;top:375px;width:194px}

  .mini{position:absolute;font-size:5.6px;line-height:1.2;text-align:justify}
  .mini .step-head{font-size:8.5px;margin-bottom:6px}
  .mini ul{list-style:none}
  .mini li{padding-left:6px;position:relative}
  .mini li::before{content:"•";position:absolute;left:0}
  .mini ol{padding-left:6px}
  .mini ol li::before{content:none}

  .box-title{font-family:"Libre Baskerville",Georgia,serif;font-size:11px;line-height:1.3;color:var(--cyan);letter-spacing:.03em;margin-bottom:8px}
  .profit .box-title{color:var(--ink)}
  .profit{color:#1d4d66}

  .portrait{position:absolute;left:196px;top:23px;width:57px;height:81px;border:2px solid var(--cyan);background:linear-gradient(160deg,#9a9a9a,#4d4d4d)}
  .author-name{position:absolute;left:155px;top:119px;width:140px;text-align:center;font-family:"Libre Baskerville",Georgia,serif;color:var(--cyan);font-size:10.5px;letter-spacing:.02em}
  .bio{left:157px;top:140px;width:136px;color:var(--body)}
</style>
</head>
<body>

<!-- Cover -->
<section class="page cover">
  <svg class="frame" viewBox="0 0 476 672" aria-hidden="true">
    <polygon points="0,0 402,0 0,452" fill="var(--paper)"/>
    <polygon points="402,0 416,0 0,468 0,452" fill="var(--cyan)"/>
  </svg>
  <svg class="frame" viewBox="0 0 476 672">
    <polygon role="img" aria-label="Line drawing of a three-storey apartment building with a blue outline" points="108,502 128,416 162,420 175,378 212,340 240,360 330,252 378,296 408,314 476,430 476,540 108,540" fill="var(--slate-light)"/>
  </svg>
  <h1 class="title">MULTIFAMILY<br>CASHFLOW<br>INVESTMENT<br>STRATEGY</h1>
  <p class="tagline">Turning Underperforming Multifamily Properties into Highly Profitable, Cash-Flowing Assets.</p>
</section>

<!-- 3 Steps -->
<section class="page steps">
  <svg class="frame" viewBox="0 0 475 672" aria-hidden="true">
    <polygon points="0,0 218,0 0,262" fill="var(--paper)"/>
    <polygon points="218,0 230,0 0,276 0,262" fill="var(--cyan)"/>
  </svg>
  <svg class="frame" viewBox="0 0 475 672">
    <polygon role="img" aria-label="Line drawing of a modern apartment building corner with a blue outline" points="118,262 130,160 158,160 165,110 230,44 265,70 310,20 364,60 444,128 475,212 475,300 118,300" fill="var(--slate-light)"/>
  </svg>
  <h2 class="title running-head">MULTIFAMILY<br>CASHFLOW<br>INVESTMENT<br>STRATEGY</h2>
  <h3 class="section-title">3 STEPS FOR SUCCESS</h3>
  <div class="col col-a" style="top:372px;left:27px;width:218px">
    <h4 class="step-head">1. Buy Right:</h4>
    <div style="padding-left:9px">
      <p>Value Add - Key questions when considering a property:<br><i>• Who owns it?</i><br><i>• How long have they owned it?</i><br><i>• Why are they selling it?</i></p>
      <p style="margin-bottom:0">What to look for:</p>
      <ol style="position:relative">
        <li style="position:relative"><b>A.</b><i>Poor management -</i> typically by individual owners, families, or out of state management.</li>
        <li style="position:relative"><b>B.</b><i>Under market rents -</i> rates significantly below comparable prices in the area.</li>
        <li style="position:relative"><b>C.</b><i>Deferred maintenance -</i> this can be a sign of a motivated or “burned-out” seller. Light exterior and interior upgrades, e.g., paint, landscaping, carpet replacement, fixture and appliance upgrades, will have a significant impact.</li>
        <li style="position:relative"><b>D.</b><i>High vacancy -</i> often due to poor marketing.</li>
        <li style="position:relative"><b>E.</b><i>Motivated sellers -</i> allows for negotiation a lower price. Common motivators include divorce, bankruptcy, retirement, inherited properties, new investment opportunity, burnout, etc.</li>
        <li style="position:relative"><b>F.</b><i>Owner paid utilities -</i> allows for significant upside in income through implementing Ratio Utility Business System (RUBS). By tackling these issues, we will successfully reposition the property, which</li>
      </ol>
    </div>
  </div>
  <div class="col col-b" style="top:378px;left:259px;width:190px">
    <p style="padding-left:8px;margin-bottom:0">will significantly increase the income. As a result, the value of the property will also increase.</p>
    <ul class="dots">
      <li>Property Class - B and C class properties in A and B neighborhoods - Prefer 1980’s or newer.</li>
      <li>These properties tend to house blue collar workers; don’t compete with new(er) construction; and don’t share the same challenges as C and D properties in C and D neighborhoods, which can encounter issues with crime, major disrepair, and increased vulnerability to economic downturns.</li>
      <li>Market Analysis - Target emerging markets with population and job growth; low to median cost of housing which allows rent growth (e.g., Columbus, Oklahoma, Atlanta, Dallas, Phoenix); median income of ~$35k/yr; and landlord and business friendly rules and regulations (e.g., Ohio, Texas, Florida, Oklahoma, Colorado).</li>
      <li>Scale - 60+ units to support effective, third-party professional management. Additionally, targeting 60+ units will increase the likelihood of stability by creating a buffer against tenant turnover and other unplanned expenses.</li>
      <li>Cash flow - The property must generate cash flow from day one, before value add strategies are deployed.</li>
      <li>Buy on actual numbers instead of on pro forma analysis, which project or estimate financial return.</li>
    </ul>
  </div>
</section>

<!-- Finance & Manage -->
<section class="page finance">
  <svg class="frame" viewBox="0 0 306 434" aria-hidden="true">
    <polygon points="0,0 146,0 0,168" fill="var(--paper)"/>
    <polygon points="146,0 154,0 0,178 0,168" fill="var(--cyan)"/>
  </svg>
  <svg class="frame" viewBox="0 0 306 434">
    <polygon role="img" aria-label="Line drawing of an apartment building with a blue outline" points="14,360 20,300 50,290 95,206 135,240 150,230 210,290 250,300 278,362 306,368 306,434 14,434" fill="var(--slate-light)"/>
  </svg>
  <h2 class="title small-head">MULTIFAMILY<br>CASHFLOW<br>INVESTMENT<br>STRATEGY</h2>
  <div class="mini" style="left:157px;top:22px;width:132px">
    <h4 class="step-head">2. Finance Right:</h4>
    <ul>
      <li>Longterm debt - with long terms and amortization periods.</li>
      <li>Non-recourse if possible, e.g., agency lenders and CMBS. There is an extremely low foreclosure rate for agency underwritten properties (1%-2%).</li>
      <li>No prepayment penalty.</li>
      <li>No due on sale clause.</li>
    </ul>
    <h4 class="step-head" style="margin-top:12px">3. Manage Right:</h4>
    <ul>
      <li>Third-Party Management with experience in this specific class of multifamily real estate.</li>
      <li>Sizable but not too large that our property gets lost.</li>
      <li>Only in property management, not acquisition or development so that there is no conflict of interest.</li>
      <li>Use of Sole Purpose Entity Structures, e.g., LLC’s for asset protection.</li>
      <li>Optimization through use of systems.</li>
      <li>Tenant satisfaction - Ensure great customer service to the tenant, e.g., 24 hour response to maintenance requests, cleanliness, and security. Happy tenants who feel heard and cared for, don’t leave, which limits tenant turnover, and lowers expenses.</li>
      <li>Increase the “curb appeal” - Freshened exterior with modern paint schemes, landscaping, and new signage. Rebranding with a name change, webpage, etc.</li>
    </ul>
  </div>
</section>

<!-- Strategies & Profit -->
<section class="page income">
  <svg class="frame" viewBox="0 0 306 434">
    <polygon points="0,0 142,0 0,172" fill="var(--paper)" aria-hidden="true"/>
    <polygon points="142,0 150,0 0,182 0,172" fill="var(--cyan)" aria-hidden="true"/>
    <rect x="11" y="19" width="285" height="205" fill="none" stroke="var(--paper)" stroke-width="3"/>
    <polygon role="img" aria-label="Small line drawing of an apartment building" points="16,168 40,130 62,122 90,140 110,150 130,200 130,220 16,220" fill="var(--slate-light)"/>
    <rect x="11" y="250" width="285" height="165" fill="var(--cyan)" stroke="var(--paper)" stroke-width="3"/>
    <polygon role="img" aria-label="Line drawing of an apartment building on blue" points="170,330 180,290 230,252 262,276 280,270 296,300 296,412 170,412" fill="var(--cyan-deep)"/>
    <polygon points="306,282 306,434 174,434" fill="var(--paper)" aria-hidden="true"/>
  </svg>
  <h2 class="title small-head">MULTIFAMILY<br>CASHFLOW<br>INVESTMENT<br>STRATEGY</h2>
  <div class="mini" style="left:141px;top:34px;width:146px">
    <h4 class="box-title">5 STRATEGIES<br>FOR INCREASING<br>INCOME</h4>
  </div>
  <div class="mini" style="left:141px;top:86px;width:146px;font-size:5px">
    <ol>
      <li>1. Fill vacant units at market rate
        <ul><li>After light renovation (&lt; $1,000 per unit) - modern, two-tone paint schemes, vinyl wood plank flooring to replace carpet; cleaning of existing carpet.</li></ul></li>
      <li>2. Employ RUBS, where applicable
        <ul><li>Pre-calculated formula for billing back a tenant’s utilities.</li><li>Water, sewer, trash, gas/electric.</li></ul></li>
      <li>3. Gradually raise existing tenants to market rate AFTER adding value
        <ul><li>Improve the exterior “curb appeal” - power washing, landscaping, painting.</li></ul></li>
      <li>4. Fees - Pet fees; deposits; late fees; move-in fees</li>
      <li>5. Laundry machines</li>
      <li>6. Lower expenses through renegotiation of contracts</li>
    </ol>
  </div>
  <div class="mini profit" style="left:22px;top:262px;width:140px;font-size:5px">
    <h4 class="box-title">5 WAYS TO PROFIT</h4>
    <ol style="padding-left:0">
      <li>1. Monthly Cash Flow - From day one. Conservative estimate of 8% or higher cash on cash return.</li>
      <li>2. Equity through principal pay down - As the tenants pay down the mortgage, your equity continues to increase and creates true wealth.</li>
      <li>3. Reduced or even elimination of taxes through depreciation by doing cost segregation.</li>
      <li>4. Cash out refinancing - into non-recourse debt (if not already); return of original capital plus additional monies that can be used towards reinvestment into the asset and future assets.</li>
      <li>5. Forced Appreciation - by repositioning the asset through the methods previously discussed. Potential to double the original investment at the time of sale, which could occur in 5-7 years or sooner depending on the market.</li>
    </ol>
  </div>
</section>

<!-- Author -->
<section class="page author">
  <svg class="frame" viewBox="0 0 306 434" aria-hidden="true">
    <polygon points="0,0 146,0 0,168" fill="var(--paper)"/>
    <polygon points="146,0 154,0 0,178 0,168" fill="var(--cyan)"/>
  </svg>
  <svg class="frame" viewBox="0 0 306 434">
    <polygon role="img" aria-label="Line drawing of an apartment building with a blue outline" points="14,362 20,300 50,290 95,206 135,240 150,230 210,290 250,300 278,362 306,368 306,434 14,434" fill="var(--slate-light)"/>
  </svg>
  <h2 class="title small-head">MULTIFAMILY<br>CASHFLOW<br>INVESTMENT<br>STRATEGY</h2>
  <div class="portrait" role="img" aria-label="Headshot of the author"></div>
  <h3 class="author-name">DANELLE ASHWORTH</h3>
  <p class="mini bio">Danelle Ashworth is a real estate investor and physician with a passion for identifying and fixing problems through innovative and creative solutions. Her transition into commercial real estate is merely an extension of that passion. It is her professional experience in a demanding and competitive field, along with her tenacity and discipline for doing things effectively and efficiently, which instills confidence in her success as a CRE investor.</p>
</section>

</body>
</html>
```